SCXN Banner Ad Design

We need a banner ad design for the Scholarly Capital Exchange Network (SCXN). SCXN is an internet-based consortium whose goal is to empower the global population to invest efficiently in financial markets by learning to apply a variety of quantitative stock market prediction techniques developed by professors at top U.S. universities. These techniques have good predictive performance for different classes of financial assets comparable to large existing mutual funds in the US. With the advent of online trading platforms, an increasing number of individual investors participate in the stock market. However, most individuals lack awareness about the existence of these academic prediction methods. Also, personalized decision-making based on these methods cannot be achieved without the application of optimal quantitative tools.
SCXN makes these prediction methods, and the tools for the optimal allocation of resources between different assets, freely available to the general public through a web platform that allows the user to a) learn about the extensive research at top U.S. universities that shows financial markets have a predictable component and identify models and asset classes that suit their investment preferences and objectives; b) back test these diverse trading models, using decades of historical stock market data, that provide returns in line with top investment houses and funds; c) obtain future predictions based on the underlying models; d) update the amounts invested in each of several assets at regular intervals of time according to the predictions of these models; e) track the performance of his portfolio in real time; f) build his financial social network whereby he can gain insights from other users as well as mirror their trading strategies in real time; and g) access leading financial experts from both academia and industry, who are available to provide advice and answer questions. All of the above features are novel additions to internet-based resources available to the average user.
The banner ad will be used on several websites, but first likely on CareerLoop (a social network for job searches) and CodeHarbor (an online community for software developers/engineers). The ad should capture the theme (and SCXN’s mission) of empowering the individual investor (along with the academic emphasis of the site) and leave a little room to be able to custom tailor it to a specific user demographic. For example, on CodeHarbor the goal is to target tech savvy individuals who undertake financial investments on their own, so we will need room on the ad itself to insert a “catch phrase” that speaks to these users specifically. Similarly, on CareerLoop, we may opt to target financial asset managers and so will insert a phrase into the ad that reaches out to these types of users. You can insert a few different phrases that you come up with on different versions of the ad intended for different groups of users. Here are also a few sample "catch phrases" for you to work with:
SCXN - Control Your Investments Without The Fees
SCXN – Beat the Market. Without The Fees.
SCXN – Hack the Markets. Without the Fees.
The SCXN Beta– Hack the Ivory Tower.
SCXN – Democratizing The Investment Landscape
Finally, we are open to different color schemes, but for reference the current version of the SCXN site uses a bluish theme.

```html
<!DOCTYPE html>
<html lang="en">
<head>
<meta charset="utf-8">
<title>SCXN Banner</title>
<link href="https://fonts.googleapis.com/css2?family=Roboto+Condensed:wght@700&display=swap" rel="stylesheet">
<style>
  :root {
    --bg: #ffffff;
    --navy: #1f3f6b;
    --blue: #1b5fa8;
    --orange: #f7941d;
    --art-blue: #3d8fd9;
    --art-gold: #e0b43a;
  }
  html, body {
    margin: 0;
    padding: 0;
    overflow: hidden;
    background: var(--bg);
  }
  .banner {
    position: relative;
    width: 1200px;
    height: 148px;
    background: var(--bg);
    overflow: hidden;
    font-family: "Roboto Condensed", "Arial Narrow", sans-serif;
  }
  .brand {
    position: absolute;
    left: 14px;
    top: 50px;
    display: flex;
    align-items: center;
    gap: 10px;
  }
  .brand-mark {
    width: 14px;
    height: 14px;
    background: var(--orange);
    flex: none;
  }
  .brand-name {
    font-size: 44px;
    font-weight: 700;
    color: var(--navy);
    line-height: 1;
    letter-spacing: 2px;
  }
  .headlines {
    position: absolute;
    left: 300px;
    width: 500px;
    top: 7px;
    margin: 0;
    padding: 0;
    list-style: none;
    text-align: center;
  }
  .headline {
    font-size: 28px;
    font-weight: 700;
    line-height: 43px;
    letter-spacing: -0.3px;
    white-space: nowrap;
  }
  .headline .action { color: var(--orange); }
  .headline .promise { color: var(--blue); }
  .mascot-art {
    position: absolute;
    left: 915px;
    top: 0;
    width: 270px;
    height: 148px;
    background: linear-gradient(100deg, #eef4fb 0%, #cfe2f6 35%, var(--art-blue) 55%, var(--art-gold) 75%, #f6dc86 100%);
    border-radius: 6px;
    opacity: 0.85;
  }
</style>
</head>
<body>
  <div class="banner">
    <div class="brand">
      <span class="brand-mark"></span>
      <span class="brand-name">SCXN</span>
    </div>

    <ul class="headlines">
      <li class="headline"><span class="action">Control Your Investments</span> <span class="promise">Without the Fees</span></li>
      <li class="headline"><span class="action">Beat the Markets</span> <span class="promise">Without the Fees</span></li>
      <li class="headline"><span class="action">Hack the Markets</span> <span class="promise">Without the Fees</span></li>
    </ul>

    <div class="mascot-art" role="img" aria-label="Blue figure pushing a large gold coin marked with a dollar sign"></div>
  </div>
</body>
</html>
```